Family Farm Looking for meat label

We have a small farm in Italy with two types of cow "Piemontese" and "Pezzata Rossa Valdostana". We need label ( about 5x5 cm) to put on the boxes and on every single piece of meat.

Target Market(s)

private client

Industry/Entity Type

family farm

Colors

Designer to choose colors to be used in the design.

Requirements
Must have
• to write "Azienda Agricola Il Roveto" and the cow like our cow not differently. the Piemontese breed cow has the typical physical shapes as in the photo. No photo on the label just a drawing o something like that.
Nice to have
• just a one label, clear, fine and clean . Maybe with pastel color or watercolor. We are a small family farm.
Should not have
• no photo, no another type of cow

```html
<!DOCTYPE html>
<html lang="it">
<head>
<meta charset="utf-8">
<title>Etichette carne – Azienda Agricola Il Roveto</title>
<link rel="stylesheet" href="https://fonts.googleapis.com/css2?family=Roboto:wght@700&display=swap">
<style>
  :root {
    --farm-green: #30b253;
    --paper: #ffffff;
    --backdrop: #ffffff;
    --shadow: rgba(0, 0, 0, 0.38);
  }
  * { box-sizing: border-box; margin: 0; padding: 0; }
  html, body {
    width: 1200px;
    height: 742px;
    overflow: hidden;
    background: var(--backdrop);
  }
  body {
    position: relative;
    font-family: "Roboto", Arial, sans-serif;
    font-weight: 700;
  }
  .meat-label {
    position: absolute;
    top: 186px;
    width: 378px;
    height: 378px;
    background: var(--paper);
    box-shadow: 7px 8px 9px var(--shadow);
    overflow: hidden;
  }
  .meat-label--piemontese { left: 161px; }
  .meat-label--valdostana { left: 626px; }

  .breed-area {
    position: absolute;
    inset: 0 0 auto 0;
    height: 112px;
    display: flex;
    align-items: center;
    justify-content: center;
    padding-right: 8px;
  }
  .breed-name {
    color: var(--farm-green);
    font-size: 26px;
    line-height: 32px;
    text-align: center;
  }
  .hang-hole {
    position: absolute;
    width: 33px;
    height: 33px;
    border-radius: 50%;
    z-index: 2;
  }
  .hang-hole--top {
    left: 330px;
    top: 15px;
    border: 5px solid var(--farm-green);
  }
  .hang-hole--band {
    left: 21px;
    top: 222px;
    border: 5px solid var(--paper);
  }
  .farm-band {
    position: absolute;
    left: 0;
    right: 0;
    top: 112px;
    bottom: 0;
    background: var(--farm-green);
  }
  .roof-shape {
    position: absolute;
    left: 0;
    top: 0;
    width: 378px;
    height: 378px;
  }
  .farm-title {
    position: absolute;
    left: 0;
    right: 0;
    top: 137px;
    color: var(--paper);
    font-size: 30px;
    line-height: 35px;
    text-align: center;
    padding-left: 2px;
    z-index: 2;
  }
  .cow-drawing {
    position: absolute;
    left: 97px;
    top: 286px;
    width: 94px;
    height: 28px;
    background: var(--farm-green);
    border-radius: 3px;
  }
  .farm-mark {
    position: absolute;
    left: 31px;
    top: 316px;
    color: var(--farm-green);
    font-size: 46px;
    line-height: 47px;
    white-space: nowrap;
  }
</style>
</head>
<body>
  <article class="meat-label meat-label--piemontese">
    <div class="breed-area">
      <p class="breed-name">PIEMONTESE</p>
    </div>
    <span class="hang-hole hang-hole--top"></span>
    <div class="farm-band"></div>
    <svg class="roof-shape" viewBox="0 0 378 378" aria-hidden="true">
      <polygon points="0,313 144,231 378,362 378,378 0,378" fill="#ffffff"/>
      <line x1="240" y1="264" x2="380" y2="341" stroke="#ffffff" stroke-width="6"/>
    </svg>
    <h1 class="farm-title">AZIENDA AGRICOLA<br>IL ROVETO</h1>
    <span class="hang-hole hang-hole--band"></span>
    <div class="cow-drawing" role="img" aria-label="Disegno di una mucca Piemontese con animali da cortile"></div>
    <p class="farm-mark">IL ROVETO</p>
  </article>

  <article class="meat-label meat-label--valdostana">
    <div class="breed-area">
      <p class="breed-name">PEZZATA ROSSA<br>VALDOSTANA</p>
    </div>
    <span class="hang-hole hang-hole--top"></span>
    <div class="farm-band"></div>
    <svg class="roof-shape" viewBox="0 0 378 378" aria-hidden="true">
      <polygon points="0,313 144,231 378,362 378,378 0,378" fill="#ffffff"/>
      <line x1="240" y1="264" x2="380" y2="341" stroke="#ffffff" stroke-width="6"/>
    </svg>
    <h1 class="farm-title">AZIENDA AGRICOLA<br>IL ROVETO</h1>
    <span class="hang-hole hang-hole--band"></span>
    <div class="cow-drawing" role="img" aria-label="Disegno di una mucca Pezzata Rossa Valdostana con animali da cortile"></div>
    <p class="farm-mark">IL ROVETO</p>
  </article>
</body>
</html>
```